Foot and ankle surgeon requires a website design

I need a website where prospective and established patients can obtain information and then direct them to making appointments. My practice is a highly professional surgical practice specialising in surgery to the foot and ankle. My title is Mr Colin Dwyer, Podiatric Foot & Ankle Surgeon. My qualifications are: BSc MSc FACPS
The practice website will require information on: Locations, phone numbers to make appointments, general background on podiatric surgery,
I would like to include information on: my hospital appointments, surgical fellowships held, training programs undertaken, association memberships, publications written, links to useful websites
A page dedicated to common foot conditions would be useful and also a page with referral information including an online registration section that will be sent direct to the receptionist.
Examples of similar websites include:
http://www.trevorkeplinfeet.com.au/
http://www.vollardfootsurgeon.com.au/
I will provide files on logo, self photos and my personal training history etc.
Also if there is going to be a background theme I personally am associated with surfing and beach activities, it would be great if this was able to be reflected in the design.
Thank you.

```html
<!DOCTYPE html>
<html lang="en">
<head>
<meta charset="utf-8">
<title>Mr Colin Dwyer — Podiatric Foot &amp; Ankle Surgeon</title>
<link href="https://fonts.googleapis.com/css2?family=Open+Sans:wght@400;600;700&display=swap" rel="stylesheet">
<style>
:root{
  --blue:#1d4f7c;
  --blue-dark:#163d61;
  --navy:#12324f;
  --orange:#f47a20;
  --text:#555b61;
  --muted:#8a9097;
  --line:#dfe3e6;
  --panel:#efefef;
  --white:#ffffff;
}
*{box-sizing:border-box;margin:0;padding:0}
html,body{width:1200px;height:2380px;overflow:hidden;background:var(--white)}
body{font-family:"Open Sans",Arial,sans-serif;color:var(--text);font-size:15px;line-height:1.55}
.wrap{width:1060px;margin:0 auto;position:relative}
ul{list-style:none}

/* header */
.site-header{height:90px;position:relative}
.topbar{position:absolute;right:70px;top:0;background:var(--blue);color:var(--white);font-size:13px;padding:3px 14px;display:flex;gap:22px;border-radius:0 0 4px 4px}
.topbar span{display:flex;align-items:center;gap:6px}
.brand{position:absolute;left:70px;top:14px;display:flex;align-items:center;gap:12px}
.brand-mark{width:46px;height:46px;border-radius:50%;background:var(--blue)}
.brand-name{font-size:25px;font-weight:700;color:var(--blue);line-height:1.1}
.brand-tag{font-size:12px;color:var(--orange);font-weight:600}
.main-nav{position:absolute;right:70px;top:44px;display:flex;gap:8px}
.main-nav a{font-size:13px;font-weight:600;color:var(--blue);text-decoration:none;padding:6px 16px;border-radius:3px;letter-spacing:.5px}
.main-nav a.active{background:var(--orange);color:var(--white)}

/* hero */
.hero{height:655px;position:relative;border-bottom:6px solid var(--orange)}
.hero-photo{position:absolute;inset:0;background:linear-gradient(180deg,#9cc3e3 0%,#d7e8f5 45%,#e9cbb6 70%,#f3f5f8 100%)}
.hero-copy{position:absolute;left:0;right:0;top:120px;text-align:center}
.hero-copy .line{display:inline-block;color:var(--white);font-weight:700;font-size:40px;padding:4px 22px;letter-spacing:.5px}
.line.one{background:var(--orange)}
.line.two{background:var(--blue);margin-top:10px;font-size:37px}
.hero-dots{position:absolute;left:0;right:0;bottom:14px;display:flex;justify-content:center;gap:8px}
.hero-dots i{width:12px;height:12px;border-radius:50%;background:var(--white);opacity:.8}
.hero-dots i.on{background:var(--orange);opacity:1}

/* services */
.services{padding:46px 0 40px}
.section-title{text-align:center;font-size:30px;color:var(--blue);font-weight:600}
.section-title em{font-style:normal;color:var(--orange)}
.title-rule{width:60px;height:3px;background:var(--orange);margin:8px auto 0}
.service-grid{display:flex;gap:40px;margin-top:40px}
.service{flex:1;display:flex;gap:18px}
.service-icon{flex:0 0 72px;height:72px;border-radius:50%;border:3px solid var(--orange);display:flex;align-items:center;justify-content:center}
.service h3{font-size:22px;color:var(--blue);font-weight:600}
.service p{font-size:14px;margin:6px 0 12px}
.btn{display:inline-block;background:var(--blue);color:var(--white);font-size:13px;padding:6px 16px;border-radius:4px;text-decoration:none}

/* about */
.about{background:var(--panel);padding:56px 0 60px;height:412px}
.about .wrap{display:flex;gap:60px}
.about-text{flex:1}
.about h2{font-size:30px;font-weight:600;color:var(--blue)}
.about h2 em{font-style:normal;color:var(--orange)}
.about .rule{width:60px;height:3px;background:var(--orange);margin:8px 0 22px}
.about p{font-size:15px;margin-bottom:22px}
.about-screen{flex:0 0 400px}

/* news & calendar */
.updates{padding:46px 0 0;height:500px}
.updates .wrap{display:flex;gap:60px}
.col{flex:1}
.col h2{font-size:26px;font-weight:600;color:var(--blue)}
.col h2 em{font-style:normal;color:var(--orange)}
.col .rule{width:60px;height:3px;background:var(--orange);margin:8px 0 24px}
.article{display:flex;gap:20px;margin-bottom:26px}
.article-thumb{flex:0 0 170px;height:110px;border-radius:3px}
.thumb-a{background:linear-gradient(135deg,#c9d7e4,#e8d3c2)}
.thumb-b{background:linear-gradient(135deg,#e3c8ad,#f1e6da)}
.item-title{font-size:15px;font-weight:700;color:#333;text-transform:uppercase}
.item-text{font-size:14px;margin-top:4px}
.event{display:flex;gap:18px;margin-bottom:18px}
.date{flex:0 0 58px;text-align:center;border:1px solid var(--line);border-radius:3px;overflow:hidden;height:60px}
.date b{display:block;background:var(--orange);color:var(--white);font-size:12px;padding:2px 0}
.date span{font-size:22px;font-weight:700;color:var(--blue)}

/* footer */
.site-footer{background:var(--blue);color:#cfdbe7;height:308px;padding-top:40px}
.site-footer .wrap{display:flex;gap:40px}
.fcol{flex:1}
.fcol h4{color:var(--white);font-size:17px;font-weight:600;padding-bottom:10px;border-bottom:1px solid #3a6a95;margin-bottom:12px}
.fcol li{font-size:13px;padding:3px 0;display:flex;align-items:center;gap:8px}
.fcol li::before{content:"";width:5px;height:5px;border-right:2px solid var(--orange);border-top:2px solid var(--orange);transform:rotate(45deg)}
.contact li::before{display:none}
.socials{display:flex;gap:8px;margin-top:10px}
.socials i{width:26px;height:26px;border-radius:50%;background:var(--white);opacity:.9}
.signup p{font-size:13px}
.signup .field{height:30px;background:var(--white);margin-top:10px;border-radius:3px;color:#999;font-size:12px;padding:5px 10px}
.signup .submit{display:inline-block;background:var(--orange);color:var(--white);font-size:12px;font-weight:700;padding:5px 18px;border-radius:3px;margin-top:8px}
.bottom-bar{background:var(--navy);height:40px;color:#9fb5ca;font-size:12px}
.bottom-bar .wrap{display:flex;justify-content:space-between;align-items:center;height:40px}
</style>
</head>
<body>

<header class="site-header">
  <div class="topbar">
    <span><svg width="14" height="10" viewBox="0 0 14 10"><rect x=".5" y=".5" width="13" height="9" fill="none" stroke="#fff"/><path d="M.5 .5 7 6 13.5 .5" fill="none" stroke="#fff"/></svg>reception@dwyerfootclinic.com.au</span>
    <span><svg width="12" height="12" viewBox="0 0 12 12"><path d="M2 1l2 0 1 3-1.5 1a7 7 0 0 0 3.5 3.5L8 7l3 1v2a1 1 0 0 1-1 1A9 9 0 0 1 1 2a1 1 0 0 1 1-1z" fill="#fff"/></svg>02 5550 1482</span>
  </div>
  <div class="brand">
    <div class="brand-mark"></div>
    <div>
      <div class="brand-name">Mr Colin Dwyer</div>
      <div class="brand-tag">Podiatric Foot &amp; Ankle Surgeon</div>
    </div>
  </div>
  <nav class="main-nav">
    <a class="active" href="#">HOME</a><a href="#">SERVICES</a><a href="#">ABOUT US</a><a href="#">LOCATIONS</a><a href="#">CONTACT US</a>
  </nav>
</header>

<section class="hero">
  <div class="hero-photo" role="img" aria-label="Photo of bare feet resting on a bed against a bright window"></div>
  <div class="hero-copy">
    <div class="line one">Heading or Tagline goes here</div><br>
    <div class="line two">Second line sample goes here</div>
  </div>
  <div class="hero-dots"><i class="on"></i><i></i><i></i><i></i></div>
</section>

<section class="services">
  <div class="wrap">
    <h2 class="section-title">Services <em>Offered</em></h2>
    <div class="title-rule"></div>
    <div class="service-grid">
      <div class="service">
        <div class="service-icon"><svg width="34" height="34" viewBox="0 0 34 34"><ellipse cx="12" cy="20" rx="6" ry="10" fill="#f47a20"/><ellipse cx="23" cy="14" rx="5" ry="9" fill="#f47a20"/></svg></div>
        <div><h3>Service name</h3><p>Clear advice on foot and ankle surgery, from first visit to full recovery.</p><a class="btn" href="#">Read more</a></div>
      </div>
      <div class="service">
        <div class="service-icon"><svg width="34" height="34" viewBox="0 0 34 34"><rect x="4" y="9" width="26" height="20" rx="3" fill="#f47a20"/><rect x="12" y="5" width="10" height="6" rx="2" fill="none" stroke="#f47a20" stroke-width="2"/><path d="M17 13v12M11 19h12" stroke="#fff" stroke-width="3"/></svg></div>
        <div><h3>Service name</h3><p>Clear advice on foot and ankle surgery, from first visit to full recovery.</p><a class="btn" href="#">Read more</a></div>
      </div>
      <div class="service">
        <div class="service-icon"><svg width="34" height="34" viewBox="0 0 34 34"><circle cx="16" cy="6" r="3" fill="#f47a20"/><path d="M16 10v10h8l3 8" fill="none" stroke="#f47a20" stroke-width="3"/><path d="M12 16a8 8 0 1 0 10 11" fill="none" stroke="#f47a20" stroke-width="3"/></svg></div>
        <div><h3>Service name</h3><p>Clear advice on foot and ankle surgery, from first visit to full recovery.</p><a class="btn" href="#">Read more</a></div>
      </div>
    </div>
  </div>
</section>

<section class="about">
  <div class="wrap">
    <div class="about-text">
      <h2>About <em>Mr. Colin Dwyer</em></h2>
      <div class="rule"></div>
      <p>Colin Dwyer is a podiatric surgeon who treats bunions, heel pain, ankle injury and toe deformity. He trained in Australia and overseas, holds surgical fellowships and operates at several hospitals. His team explains each option plainly, so every patient knows what to expect before, during and after surgery, and can plan a safe return to work, sport and the surf.</p>
      <a class="btn" href="#">Read more</a>
    </div>
    <div class="about-screen">
      <svg width="400" height="290" viewBox="0 0 400 290">
        <rect x="10" y="0" width="380" height="235" rx="8" fill="#1b1f24"/>
        <rect x="22" y="12" width="356" height="200" fill="#8fa9bf" role="img" aria-label="Portrait of the surgeon reviewing an X-ray"/>
        <rect x="22" y="12" width="356" height="200" fill="url(#scr)"/>
        <path d="M170 235h60l10 40h-80z" fill="#c9ccd0"/>
        <rect x="130" y="272" width="140" height="8" rx="3" fill="#b5b9be"/>
        <defs><linearGradient id="scr" x1="0" y1="0" x2="1" y2="1"><stop offset="0" stop-color="#dfe8ef" stop-opacity=".6"/><stop offset="1" stop-color="#5d7890" stop-opacity=".5"/></linearGradient></defs>
      </svg>
    </div>
  </div>
</section>

<section class="updates">
  <div class="wrap">
    <div class="col">
      <h2>News &amp; <em>Publications</em></h2>
      <div class="rule"></div>
      <div class="article">
        <div class="article-thumb thumb-a" role="img" aria-label="Photo of a dancer's feet on tiptoe"></div>
        <div><div class="item-title">Article title goes here</div><p class="item-text">A short summary of the article sits here, with a link to read the rest.</p></div>
      </div>
      <div class="article">
        <div class="article-thumb thumb-b" role="img" aria-label="Photo of feet wearing ballet shoes"></div>
        <div><div class="item-title">Article title goes here</div><p class="item-text">A short summary of the article sits here, with a link to read the rest.</p></div>
      </div>
      <a class="btn" href="#">View all</a>
    </div>
    <div class="col">
      <h2>Calendar &amp; <em>Appointments</em></h2>
      <div class="rule"></div>
      <div class="event"><div class="date"><b>JUN</b><span>05</span></div><div><div class="item-title">Event title goes here</div><p class="item-text">Event details and venue appear here in one or two lines.</p></div></div>
      <div class="event"><div class="date"><b>JUN</b><span>08</span></div><div><div class="item-title">Event title goes here</div><p class="item-text">Event details and venue appear here in one or two lines.</p></div></div>
      <div class="event"><div class="date"><b>JUL</b><span>03</span></div><div><div class="item-title">Event title goes here</div><p class="item-text">Event details and venue appear here in one or two lines.</p></div></div>
      <a class="btn" href="#">View all</a>
    </div>
  </div>
</section>

<footer>
  <div class="site-footer">
    <div class="wrap">
      <div class="fcol"><h4>About</h4><ul><li>Sublink here</li><li>Sublink here</li><li>Sublink here</li><li>Sublink here</li><li>Sublink here</li></ul></div>
      <div class="fcol"><h4>Services offered</h4><ul><li>Sublink here</li><li>Sublink here</li><li>Sublink here</li><li>Sublink here</li><li>Sublink here</li></ul></div>
      <div class="fcol contact"><h4>Contact us</h4><ul><li>reception@dwyerfootclinic.com.au</li><li>02 5550 1482</li><li>02 5550 1483</li></ul><div class="socials"><i></i><i></i><i></i></div></div>
      <div class="fcol signup"><h4>Newsletter Signup</h4><p>Subscribe to get updates</p><div class="field">Email address</div><span class="submit">SUBMIT</span></div>
    </div>
  </div>
  <div class="bottom-bar"><div class="wrap"><span>Copyright © Mr Colin Dwyer 2014</span><span>FAQ &nbsp;|&nbsp; Sitemap &nbsp;|&nbsp; Privacy Policy</span></div></div>
</footer>

</body>
</html>
```